Up to the Challenge? Canadian based consulting company needs a two sided business card design

A Canadian based security risk management consulting company needs a two-sided business card design. What we do is provide advice and guidance related to emergency, security and business continuity management for small, medium and large companies to help ensure the protection of their people, assets, information, services, operations and reputation.

The final design should be simple, only one or two colours, eye catching, professional and one that makes people look at three or more times just because it looks so darn good.

I have include examples of business cards I like.

Target Market(s)

Small, medium and large companies.

Industry/Entity Type

Security

Contact Information for Business Card

Business Card Size: Standard size of 3.5" (89mm) x 2.0" (51mm) - (see full specifications and guides on PRINTA's website if required)
Card Stock: Looking to use PRINTA's Velda 32pt stock textured paper - seam colour either chili red or black
Business Name: The Harrowfield Group
Website: www.theharrowfieldgroup.example
Telephone: (555)214-0397
Name: Dana Forsythe
Position: Principle
e-mail: Dana.Forsythe@theharrowfieldgroup.example

Font styles to use
Serif

Colors
ec1f27
000000
9d9d9d
aaaaaa
606060

Requirements
Must have
• - "The Harrowfield Group" logo (see uploaded files). I have included grey scale and colour versions.
• - Business card details (as above)
Nice to have
• - One side black or grey scale.
• - Other side would likely be white.
• - Everyone likes the silver logo on the black background.
• - Small element of colour i.e. red but I'm leaning more to greyscale.
Should not have
• - A lot of colour. Keep it simple.

```html
<!DOCTYPE html>
<html lang="en">
<head>
<meta charset="utf-8">
<title>The Harrowfield Group – Business Cards</title>
<link rel="stylesheet" href="https://fonts.googleapis.com/css2?family=Cinzel:wght@500;600&family=Merriweather:wght@700&family=Montserrat:wght@400;500&display=swap">
<style>
  :root {
    --backdrop: #2a2a2a;
    --card: #050505;
    --ink: #ffffff;
    --silver: #d9d9d9;
    --grey: #9d9d9d;
    --shade: #606060;
  }
  * { box-sizing: border-box; margin: 0; padding: 0; }
  html, body {
    width: 1200px; height: 1000px; overflow: hidden;
    background: var(--backdrop);
  }
  .stage {
    position: relative; width: 1200px; height: 1000px;
    display: flex; flex-direction: column; align-items: center; justify-content: center; gap: 60px;
  }
  .card {
    position: relative; width: 700px; height: 400px;
    background: var(--card); border-radius: 22px;
    box-shadow: 0 20px 40px rgba(0,0,0,.5);
    overflow: hidden; color: var(--ink);
  }

  /* front */
  .front-brand {
    position: absolute; left: 0; right: 0; top: 100px;
    display: flex; flex-direction: column; align-items: center; gap: 18px;
  }
  .brand-mark { width: 70px; height: 70px; background: var(--silver); }
  .brand-name {
    font-family: "Cinzel", serif; font-weight: 600; font-size: 38px;
    letter-spacing: 1px; color: var(--ink); text-align: center; line-height: 1.05;
  }
  .brand-name small { display: block; font-size: 20px; letter-spacing: 4px; }
  .profile-line {
    position: absolute; left: 40px; bottom: 36px;
    font-family: "Montserrat", sans-serif; font-size: 18px; color: var(--ink);
  }

  /* back */
  .tree-art {
    position: absolute; left: 200px; top: 20px; width: 330px; height: 380px;
    background: radial-gradient(ellipse at 50% 40%, #4a4a4a 0%, #3a3a3a 45%, rgba(5,5,5,0) 75%);
  }
  .wordmark {
    position: absolute; left: 40px; top: 40px;
    font-family: "Cinzel", serif; font-weight: 600; font-size: 24px; line-height: 1;
  }
  .wordmark small { display: block; font-size: 13px; letter-spacing: 3px; margin-top: 2px; }
  .wordmark-rule {
    position: absolute; left: 40px; top: 92px; width: 310px; height: 2px; background: var(--ink);
  }
  .person { position: absolute; left: 40px; top: 110px; display: flex; gap: 14px; }
  .person-bar { width: 20px; height: 44px; background: var(--ink); margin-top: 6px; }
  .person-name {
    font-family: "Merriweather", serif; font-weight: 700; font-size: 28px; line-height: 1.1;
  }
  .person-role { font-family: "Montserrat", sans-serif; font-size: 17px; color: var(--silver); }
  .contacts {
    position: absolute; left: 74px; top: 200px; list-style: none;
    font-family: "Montserrat", sans-serif; font-size: 17px; line-height: 1.55;
  }
  .contacts li { display: flex; align-items: center; gap: 10px; }
  .contacts svg { width: 13px; height: 13px; fill: var(--ink); flex: none; }
  .corner-mark {
    position: absolute; right: 60px; top: 110px; width: 80px; height: 80px; background: var(--silver);
  }
</style>
</head>
<body>
<main class="stage">
  <section class="card card-front">
    <div class="front-brand">
      <div class="brand-mark"></div>
      <div class="brand-name">The Harrowfield<small>Group</small></div>
    </div>
    <p class="profile-line">profile: https://ca.example.com/in/danaforsythe</p>
  </section>

  <section class="card card-back">
    <div class="tree-art" role="img" aria-label="Large faint grey leafy tree illustration"></div>
    <div class="wordmark">The Harrowfield<small>Group</small></div>
    <div class="wordmark-rule"></div>
    <div class="person">
      <div class="person-bar"></div>
      <div>
        <p class="person-name">Dana Forsythe</p>
        <p class="person-role">Principle</p>
      </div>
    </div>
    <ul class="contacts">
      <li><svg viewBox="0 0 24 24"><path d="M6.6 10.8a15 15 0 0 0 6.6 6.6l2.2-2.2a1 1 0 0 1 1-.25 11.4 11.4 0 0 0 3.6.57 1 1 0 0 1 1 1V20a1 1 0 0 1-1 1A17 17 0 0 1 3 4a1 1 0 0 1 1-1h3.5a1 1 0 0 1 1 1c0 1.25.2 2.45.57 3.57a1 1 0 0 1-.25 1z"/></svg>(555)214-0397</li>
      <li><svg viewBox="0 0 24 24"><path d="M2 5h20v14H2zm2 2v.5l8 5 8-5V7zm0 3v7h16v-7l-8 5z"/></svg>Dana.Forsythe@theharrowfieldgroup.example</li>
      <li><svg viewBox="0 0 24 24"><circle cx="12" cy="12" r="10"/></svg>www.theharrowfieldgroup.example</li>
    </ul>
    <div class="corner-mark"></div>
  </section>
</main>
</body>
</html>
```